Cricket Coaching Academy Needs a Flyer For Fat Bowling Academy

We need a flyer to promote a fast bowling academy we are running.
We want to emphasise that Derek Lomas will be present and that participants will receive high performance coaching.
Places in the academy are limited
Font styles to use
Sans Serif
Requirements
Must have
- Images,contact details,information about our coaches
Nice to have
- Green Background

```html
<!DOCTYPE html>
<html lang="en">
<head>
<meta charset="utf-8">
<title>Fast Bowling Academy Flyer</title>
<link href="https://fonts.googleapis.com/css2?family=Oswald:wght@700&family=Montserrat:wght@600;700&family=Michroma&family=Lato:wght@400&display=swap" rel="stylesheet">
<style>
  :root {
    --paper: #ffffff;
    --ink: #111111;
    --panel-dark: #141414;
    --panel-mid: #2e2e2e;
    --field-green: #4fc21a;
    --field-light: #8fe03a;
    --field-deep: #2e8f10;
    --kit-blue: #2f8fd6;
    --kit-light: #5cb3ee;
    --kit-deep: #1c64a8;
    --gold: #f7b500;
    --accent-green: #5cc81e;
    --white: #ffffff;
    --footer-text: #1a1a1a;
  }
  * { margin: 0; padding: 0; box-sizing: border-box; }
  html, body { width: 1200px; height: 900px; overflow: hidden; background: var(--paper); }
  .flyer { position: relative; width: 1200px; height: 900px; background: var(--paper); }

  .hero-panel {
    position: absolute; left: 52px; top: 26px; width: 1096px; height: 740px;
    overflow: hidden; background: linear-gradient(160deg, var(--panel-mid), var(--panel-dark) 60%);
  }
  .hero-scene { position: absolute; inset: 0; }

  .promo-text { position: absolute; left: 0; width: 590px; text-align: center; transform: translateY(-50%); white-space: nowrap; }
  .title-main { top: 80px; font-family: 'Oswald', sans-serif; font-weight: 700; font-size: 82px; line-height: 1; color: var(--gold); }
  .title-sub { top: 141px; font-family: 'Montserrat', sans-serif; font-weight: 700; font-size: 34px; letter-spacing: 4px; color: var(--white); line-height: 1;
    display: flex; align-items: center; justify-content: center; gap: 18px; }
  .title-sub::before, .title-sub::after { content: ""; width: 72px; height: 2px; background: var(--white); }
  .guest-label { top: 203px; font-family: 'Michroma', sans-serif; font-size: 30px; color: var(--accent-green); line-height: 1; }
  .guest-name { top: 282px; font-family: 'Oswald', sans-serif; font-weight: 700; font-size: 96px; color: var(--gold); line-height: 1; letter-spacing: 1px; }
  .lead-in { top: 388px; font-family: 'Lato', sans-serif; font-size: 40px; letter-spacing: 1.5px; color: var(--white); line-height: 1; }
  .highlight { top: 434px; font-family: 'Oswald', sans-serif; font-weight: 700; font-size: 46px; color: var(--accent-green); line-height: 1; }
  .connector { top: 485px; font-family: 'Lato', sans-serif; font-size: 36px; color: var(--white); line-height: 1; }
  .coach-name { font-family: 'Michroma', sans-serif; font-size: 35px; color: var(--gold); line-height: 1; }
  .coach-one { top: 526px; }
  .coach-two { top: 568px; }

  .partner { position: absolute; top: 656px; transform: translateY(-50%); display: flex; align-items: center; gap: 10px;
    font-family: 'Montserrat', sans-serif; font-weight: 700; line-height: 1.05; }
  .partner-coaching { left: 40px; font-size: 24px; color: var(--white); }
  .partner-coaching .mark { width: 46px; height: 46px; border-radius: 50%; background: var(--white); flex: none; }
  .partner-store { left: 330px; font-size: 26px; color: var(--gold); text-transform: uppercase; }
  .partner-store .mark { width: 22px; height: 22px; background: var(--gold); flex: none; }

  .contact-bar { position: absolute; left: 103px; top: 832px; transform: translateY(-50%); display: flex; align-items: center; gap: 22px;
    font-family: 'Michroma', sans-serif; font-size: 19px; color: var(--footer-text); }
  .contact-item { display: flex; align-items: center; gap: 10px; }
  .contact-divider { width: 3px; height: 38px; background: var(--ink); }
</style>
</head>
<body>
<div class="flyer">
  <section class="hero-panel">
    <svg class="hero-scene" width="1096" height="740" viewBox="0 0 1096 740" aria-hidden="true">
      <defs>
        <linearGradient id="fieldGlow" x1="0" y1="0" x2="0.6" y2="1">
          <stop offset="0" stop-color="var(--field-deep)"/>
          <stop offset="0.45" stop-color="var(--field-green)"/>
          <stop offset="1" stop-color="var(--field-light)"/>
        </linearGradient>
      </defs>
      <polygon points="538,0 1096,0 1096,740 800,740" fill="url(#fieldGlow)"/>
    </svg>

    <svg class="hero-scene" width="1096" height="740" viewBox="0 0 1096 740" role="img" aria-label="Photo of a fast bowler in a blue kit mid-delivery, ball in hand, on a stadium field">
      <defs>
        <linearGradient id="playerTone" x1="0" y1="0" x2="0" y2="1">
          <stop offset="0" stop-color="var(--kit-light)"/>
          <stop offset="0.5" stop-color="var(--kit-blue)"/>
          <stop offset="1" stop-color="var(--kit-deep)"/>
        </linearGradient>
      </defs>
      <rect x="760" y="20" width="250" height="720" rx="30" fill="url(#playerTone)" opacity="0.9"/>
    </svg>

    <div class="promo-text title-main">FAST BOWLING</div>
    <div class="promo-text title-sub">ACADEMY</div>
    <div class="promo-text guest-label">SPECIAL GUEST</div>
    <div class="promo-text guest-name">DEREK LOMAS</div>
    <div class="promo-text lead-in">PARTICIPANTS WILL RECEIVE</div>
    <div class="promo-text highlight">HIGH PERFORMANCE COACHING</div>
    <div class="promo-text connector">WITH</div>
    <div class="promo-text coach-name coach-one">GLEN HARTIGAN</div>
    <div class="promo-text coach-name coach-two">ROSS PEMBERTON</div>

    <div class="partner partner-coaching"><span class="mark"></span><span>Seam Line<br>Coaching</span></div>
    <div class="partner partner-store"><span class="mark"></span><span>The Kit Locker</span></div>
  </section>

  <footer class="contact-bar">
    <div class="contact-item">
      <svg width="22" height="22" viewBox="0 0 24 24" aria-hidden="true"><path fill="var(--accent-green)" d="M6.6 10.8a15.1 15.1 0 0 0 6.6 6.6l2.2-2.2c.3-.3.7-.4 1-.2 1.1.4 2.3.6 3.6.6.6 0 1 .4 1 1V20c0 .6-.4 1-1 1A17 17 0 0 1 3 4c0-.6.4-1 1-1h3.5c.6 0 1 .4 1 1 0 1.3.2 2.5.6 3.6.1.3 0 .7-.2 1z"/></svg>
      <span>0412557301</span>
    </div>
    <div class="contact-divider"></div>
    <div class="contact-item">
      <svg width="24" height="18" viewBox="0 0 26 20" aria-hidden="true"><rect x="1" y="1" width="24" height="18" fill="var(--accent-green)"/><path d="M1 1 L13 11 L25 1" fill="none" stroke="var(--paper)" stroke-width="2"/></svg>
      <span>SEAMLINE22@MAIL.COM</span>
    </div>
  </footer>
</div>
</body>
</html>
```